Business Card - The Harborline Group

We need a business card for a new venture capital fund and innovation accelerator based in San Francisco, CA. The Harborline Group will back, fund and scale life-transforming businesses. We intend to provide capital along with strategic and tactical direction to teams running exponential organizations. We are backing great ideas for vast markets with passionate visionaries. We facilitate the rapid creation of life-transforming businesses, help invent or re-invent critical industries and move the frontier of progress for the good of humankind. Maplecrest University defines Exponential Organizations as those whose impact (cost reduction or output) is disproportionally large – at least 10x larger – compared to its peers because of the use of new organizational techniques that leverage accelerating technologies. ExOs are characterized by a massive transformative purpose (MTP), a skunkworks organization and passionate teams of brilliant mountain-climbers with technical backgrounds.

Industry/Entity Type

Business

Contact Information for Business Card

Peter Odell
Managing Director

peter@theharborlinegroup.com
+1.628.307.4190

Font styles to use
Sans Serif

Requirements
Must have
• - logo
• - website: www.theharborlinegroup.com

```html
<!DOCTYPE html>
<html lang="en">
<head>
<meta charset="utf-8">
<title>The Harborline Group – Business Card</title>
<link rel="stylesheet" href="https://fonts.googleapis.com/css2?family=Open+Sans:wght@400;600;700&display=swap">
<style>
  :root {
    --bg: #d6d6d6;
    --card: #ffffff;
    --ink: #3d3d3d;
    --muted: #5a5a5a;
    --brand-blue: #1d5aa3;
    --brand-green: #6cb144;
    --shadow: rgba(0, 0, 0, 0.22);
  }
  * { box-sizing: border-box; margin: 0; padding: 0; }
  html, body {
    width: 1200px;
    height: 852px;
    overflow: hidden;
    background: var(--bg);
    font-family: "Open Sans", Arial, sans-serif;
    color: var(--ink);
  }
  .canvas {
    position: relative;
    width: 1200px;
    height: 852px;
  }
  .card {
    position: absolute;
    width: 560px;
    height: 320px;
    background: var(--card);
    border-radius: 16px;
    box-shadow: 0 6px 18px var(--shadow);
  }
  .card--front { left: 70px; top: 80px; }
  .card--back  { left: 570px; top: 452px; }

  .brand {
    display: flex;
    align-items: center;
    gap: 14px;
  }
  .brand__dot {
    width: 34px;
    height: 34px;
    border-radius: 50%;
    background: var(--brand-green);
    flex: none;
  }
  .brand__name {
    font-weight: 700;
    color: var(--ink);
    letter-spacing: 0.5px;
  }
  .card--front .brand {
    position: absolute;
    left: 0; right: 0; top: 0; bottom: 0;
    justify-content: center;
  }
  .card--front .brand__name { font-size: 30px; }

  .card--back .brand {
    position: absolute;
    right: 32px;
    top: 30px;
    gap: 10px;
  }
  .card--back .brand__dot { width: 22px; height: 22px; }
  .card--back .brand__name { font-size: 17px; }

  .person {
    position: absolute;
    left: 40px;
    top: 104px;
  }
  .person__name {
    font-size: 20px;
    font-weight: 700;
    color: var(--brand-blue);
  }
  .person__title {
    margin-top: 6px;
    font-size: 14px;
    color: var(--muted);
  }

  .contact {
    position: absolute;
    left: 40px;
    bottom: 34px;
    list-style: none;
  }
  .contact__item {
    display: flex;
    align-items: center;
    gap: 14px;
    font-size: 15px;
    color: var(--muted);
    line-height: 1;
    margin-top: 12px;
  }
  .contact__icon {
    width: 15px;
    height: 15px;
    fill: var(--brand-blue);
    flex: none;
  }
</style>
</head>
<body>
<main class="canvas">

  <section class="card card--front" aria-label="Business card front">
    <div class="brand">
      <span class="brand__dot"></span>
      <span class="brand__name">The Harborline Group</span>
    </div>
  </section>

  <section class="card card--back" aria-label="Business card back">
    <div class="brand">
      <span class="brand__dot"></span>
      <span class="brand__name">The Harborline Group</span>
    </div>

    <div class="person">
      <p class="person__name">Peter Odell</p>
      <p class="person__title">Managing Director</p>
    </div>

    <ul class="contact">
      <li class="contact__item">
        <svg class="contact__icon" viewBox="0 0 16 16" aria-hidden="true">
          <path d="M3.5 1.5l2.6 0 1.2 3.2-1.7 1.2a8.5 8.5 0 0 0 4.5 4.5l1.2-1.7 3.2 1.2v2.6c0 .9-.7 1.6-1.6 1.6A12.5 12.5 0 0 1 1.9 3.1c0-.9.7-1.6 1.6-1.6z"/>
        </svg>
        <span>+1.628.307.4190</span>
      </li>
      <li class="contact__item">
        <svg class="contact__icon" viewBox="0 0 16 16" aria-hidden="true">
          <path d="M1 3.5h14v9H1z M1.6 4l6.4 5 6.4-5" fill="none" stroke="var(--brand-blue)" stroke-width="1.6"/>
          <path d="M1 3.5h14L8 9z"/>
        </svg>
        <span>peter@theharborlinegroup.com</span>
      </li>
      <li class="contact__item">
        <svg class="contact__icon" viewBox="0 0 16 16" aria-hidden="true">
          <circle cx="8" cy="8" r="7"/>
          <path d="M1 8h14M8 1c-2.6 3-2.6 11 0 14M8 1c2.6 3 2.6 11 0 14" fill="none" stroke="#ffffff" stroke-width="1"/>
        </svg>
        <span>www.theharborlinegroup.com</span>
      </li>
    </ul>
  </section>

</main>
</body>
</html>
```